Business card and letterhead
Larkfield Harbor Consulting
I need double sided standard sized Business Card [3.5" x 2"]
Try the font from our new logo, but another font may look better - you decide
Professional
Marta J. Oakhurst, M.A., M.P.H.
President
3186 SE Quarry Lane #215
Seattle, WA 98107
marta@larkfieldharborconsulting.com
www.larkfieldharborconsulting.com
Please place the tagline on the backside below the website address.
We want this design to be used for all employee business cards.

```html
<!DOCTYPE html>
<html lang="en">
<head>
<meta charset="utf-8">
<title>Larkfield Harbor Consulting — Business Card</title>
<link rel="stylesheet" href="https://fonts.googleapis.com/css2?family=Source+Serif+4:wght@400;600&display=swap">
<style>
  :root {
    --bg: #e9e6e1;
    --card: #ffffff;
    --green: #2e7a3c;
    --green-dark: #1f5e2c;
    --brown: #6b3d1c;
    --ink: #4a4a4a;
    --rule: #c9c9c9;
  }
  * { margin: 0; padding: 0; box-sizing: border-box; }
  html, body {
    width: 1200px; height: 780px; overflow: hidden;
    background: var(--bg);
    font-family: "Source Serif 4", Georgia, serif;
  }
  .card {
    position: absolute; left: 75px; top: 90px;
    width: 1050px; height: 600px;
    background: var(--card);
    border-radius: 28px;
    overflow: hidden;
    box-shadow: 0 10px 30px rgba(0,0,0,0.18);
  }
  .card-edges { position: absolute; inset: 0; }
  .brand {
    position: absolute; left: 80px; top: 215px; width: 270px;
    text-align: center;
  }
  .brand-mark {
    width: 56px; height: 56px; border-radius: 50%;
    background: var(--green); margin: 0 auto 18px;
  }
  .brand-name {
    color: var(--green); font-weight: 600;
    font-size: 30px; line-height: 1.1; letter-spacing: 0.5px;
  }
  .brand-tagline {
    color: var(--ink); font-size: 11px; margin-top: 8px;
  }
  .divider {
    position: absolute; left: 370px; top: 100px;
    width: 1px; height: 420px; background: var(--rule);
  }
  .person { position: absolute; left: 395px; top: 100px; }
  .person-name { color: var(--green); font-size: 30px; font-weight: 600; }
  .person-title { color: var(--brown); font-size: 22px; margin-top: 6px; }
  .address {
    position: absolute; left: 395px; top: 205px;
    color: var(--ink); font-size: 18px; line-height: 1.45;
  }
  .contacts {
    position: absolute; left: 365px; top: 320px;
    list-style: none; color: var(--ink); font-size: 18px;
  }
  .contacts li { display: flex; align-items: center; height: 36px; }
  .contacts svg { width: 20px; height: 20px; margin-right: 10px; fill: var(--green-dark); }
</style>
</head>
<body>
  <article class="card">
    <svg class="card-edges" viewBox="0 0 1050 600" aria-hidden="true">
      <path d="M0 0 H70 C40 200 40 420 95 600 H0 Z" fill="var(--green)"/>
      <path d="M70 0 C40 200 40 420 95 600" fill="none" stroke="var(--brown)" stroke-width="10"/>
      <path d="M1050 0 V600 H1000 C1010 380 980 180 900 0 Z" fill="var(--green)"/>
      <path d="M900 0 C980 180 1010 380 1000 600" fill="none" stroke="var(--brown)" stroke-width="10"/>
    </svg>

    <div class="brand">
      <div class="brand-mark"></div>
      <div class="brand-name">Larkfield Harbor Consulting</div>
      <div class="brand-tagline">Planning, research and evaluation for healthier communities</div>
    </div>

    <div class="divider"></div>

    <header class="person">
      <h1 class="person-name">Marta J. Oakhurst, M.A., M.P.H.</h1>
      <p class="person-title">President</p>
    </header>

    <address class="address" style="font-style:normal">
      3186 SE Quarry Lane #215<br>
      Seattle, WA 98107
    </address>

    <ul class="contacts">
      <li><svg viewBox="0 0 24 24"><path d="M6.6 10.8a15 15 0 0 0 6.6 6.6l2.2-2.2a1 1 0 0 1 1-.25 11 11 0 0 0 3.6.6 1 1 0 0 1 1 1V20a1 1 0 0 1-1 1A17 17 0 0 1 3 4a1 1 0 0 1 1-1h3.5a1 1 0 0 1 1 1c0 1.25.2 2.45.6 3.6a1 1 0 0 1-.25 1z"/></svg>(T) 1-877-555-0148</li>
      <li><svg viewBox="0 0 24 24"><rect x="7" y="2" width="10" height="20" rx="2"/></svg>206-555-0173</li>
      <li><svg viewBox="0 0 24 24"><rect x="4" y="4" width="16" height="16" rx="2"/></svg>406-555-0192</li>
      <li><svg viewBox="0 0 24 24"><path d="M2 5h20v14H2z M2 5l10 8 10-8" /></svg>marta@larkfieldharborconsulting.com</li>
    </ul>
  </article>
</body>
</html>
```